bRevik Equity Advisors Website

We are interested in developing a complete website and long term maintenance with the developer we choose through this contest.

Brevik is a financial consulting company. We will have a website that capitalizes on the initial costs of retaining a client by providing additional services the client needs and tyically spend using 3rd parties.

The primary function of the website will be structured as a sales tool to retain and provide financial services to the client. Also, to provide other services that are integral to starting, building, and growing a business in order to increase creditibility and maintain client loyalty.

Through a combination of in-house "white label" services as well well chosen outside professional services as "affiliates".

The website home page must be a an instant curb-side appeal and representation of our desired extraordinary image. That image is a robust, innovative (bRevik), with a sophistication that creates an instant emotion of excitement and confidence that they have finally found that "needle in the haystack" they have been seeking. The feeling that they are compelled to take action lest they lose our contact information and are doomed to sink to the mediocrity that most business accept through a lack of effort and forsite.

Reason: Emails were going to the wrong account and I didn't receive any notices of questions or designs being posted.

Target Market(s)

Startup, growth and advancing companies seeking capital and other business services such as website and corporate image design, legal, marketing, asset management, investment and business consulting, etc.

Industry/Entity Type

Financial

Requirements
Must have
• We want to see your creativity
Nice to have
Should not have

```html
<!DOCTYPE html>
<html lang="en">
<head>
<meta charset="utf-8">
<title>Brevik Capital</title>
<link rel="stylesheet" href="https://fonts.googleapis.com/css2?family=Arimo:wght@400;700&display=swap">
<style>
:root{
  --band:#050505;
  --stage:#f4f4f4;
  --brand:#2e3d8f;
  --nav:#2a2a2a;
  --ring:#2a8fd0;
  --blue-deep:#2c6fc9;
  --blue-sky:#3a9cf0;
  --blue-navy:#0d5f95;
  --blue-aqua:#2aa4d8;
  --tag:#1e7fcf;
  --muted:#444;
}
*{margin:0;padding:0;box-sizing:border-box}
html,body{width:1200px;height:900px;overflow:hidden;background:var(--band)}
.canvas{position:relative;width:1200px;height:900px;background:var(--band)}
.stage{position:absolute;left:0;top:32px;width:1200px;height:836px;
  background:radial-gradient(ellipse at 55% 45%,#ffffff 0%,var(--stage) 55%,#e6e6e6 100%)}
.brand{position:absolute;left:56px;top:238px;font-family:"Arimo",sans-serif;font-weight:700;
  font-size:44px;color:var(--brand);line-height:1;white-space:nowrap}
.nav{position:absolute;left:58px;top:343px;list-style:none;font-family:"Arimo",sans-serif;font-size:17px;color:var(--nav)}
.nav li{width:160px;height:31px;line-height:31px;display:flex;justify-content:space-between}
.art{position:absolute;left:0;top:0}
.tag{position:absolute;left:418px;top:484px;width:222px;height:30px;background:var(--tag);
  color:#fff;font-family:"Arimo",sans-serif;font-weight:700;font-size:13px;line-height:30px;text-align:right;padding-right:10px;letter-spacing:.5px}
.intro{position:absolute;left:782px;top:327px;width:240px;font-family:"Arimo",sans-serif;font-size:13px;line-height:27px;color:#fff;white-space:nowrap}
.tools{position:absolute;left:996px;top:628px;font-family:"Arimo",sans-serif;font-size:15px;color:var(--muted);list-style:none}
.tools li{display:flex;align-items:center;height:28px}
.tools i{display:inline-block;width:30px;height:17px;border:2px solid #888;border-radius:4px;background:#ddd;margin-right:10px}
</style>
</head>
<body>
<div class="canvas">
  <div class="stage">
    <svg class="art" width="1200" height="836" viewBox="0 0 1200 836">
      <defs>
        <radialGradient id="shadow" cx="50%" cy="50%" r="50%"><stop offset="0" stop-color="#999" stop-opacity=".8"/><stop offset="1" stop-color="#999" stop-opacity="0"/></radialGradient>
        <linearGradient id="photo" x1="0" y1="0" x2="0" y2="1"><stop offset="0" stop-color="#f2f2f2"/><stop offset=".5" stop-color="#c9b8ad"/><stop offset="1" stop-color="#3b3b42"/></linearGradient>
      </defs>
      <ellipse cx="720" cy="738" rx="340" ry="22" fill="url(#shadow)"/>
      <circle cx="582" cy="406" r="190" fill="#fff" stroke="var(--ring)" stroke-width="12"/>
      <circle cx="582" cy="406" r="181" fill="url(#photo)" role="img" aria-label="Photo of a thoughtful businesswoman at a laptop"/>
      <circle cx="1046" cy="440" r="68" fill="var(--blue-navy)"/>
      <circle cx="1032" cy="285" r="82" fill="var(--blue-sky)"/>
      <circle cx="895" cy="388" r="150" fill="var(--blue-deep)"/>
      <circle cx="732" cy="511" r="77" fill="var(--blue-aqua)"/>
    </svg>
    <h1 class="brand">Brevik Capital</h1>
    <ul class="nav">
      <li><span>HOME</span><span>&gt;</span></li>
      <li><span>ABOUT US</span><span>&gt;</span></li>
      <li><span>SERVICES</span><span>&gt;</span></li>
      <li><span>CLIENTS</span><span>&gt;</span></li>
      <li><span>COMPANY</span><span>&gt;</span></li>
      <li><span>CONTACT US</span><span>&gt;</span></li>
    </ul>
    <div class="tag">NEWS AND EVENTS</div>
    <p class="intro">Through a combination of<br>in-house "white label" services as<br>well well chosen outside profes-<br>sional services as "affiliates".</p>
    <ul class="tools">
      <li><i></i>fullscreen</li>
      <li><i></i>copyright</li>
    </ul>
  </div>
</div>
</body>
</html>
```